Letterhead Design for Law Firm that Specializes in Property Damage Litigation

We are looking for a redesign of our letterhead. Our current letterhead lists all of our current staff members and we'd like to come up with a design that does NOT list all of the staff members so that it does not need to be updated with every newly hired employee. Must be in editable format.

We are a law firm that specializes in property damage, so we need something that is professional, yet modern. The final design should use our existing logo and should use a blue color scheme (alternate colors would be gray, black, and white).

Industry/Entity Type

Legal

Colors
0054AA
0677BA
7BADD7
CADEEF
E8F1F8

```html
<!DOCTYPE html>
<html lang="en">
<head>
<meta charset="utf-8">
<title>Ashford Kellan Moore — Letterhead</title>
<link href="https://fonts.googleapis.com/css2?family=Open+Sans:wght@400;600;700&display=swap" rel="stylesheet">
<style>
  :root {
    --navy: #24508a;
    --blue-pale: #e8f1f8;
    --gray: #7a7d82;
    --gray-light: #b9bcc0;
    --text: #55585d;
    --paper: #ffffff;
    --backdrop: #e4e5e7;
  }
  * { margin: 0; padding: 0; box-sizing: border-box; }
  html, body {
    width: 1200px; height: 800px; overflow: hidden;
    background: var(--backdrop);
  }
  .canvas {
    width: 1200px; height: 800px;
    display: flex; align-items: center; justify-content: center;
  }
  .letterhead {
    position: relative;
    width: 530px; height: 750px;
    background: var(--paper);
    box-shadow: 0 6px 24px rgba(0,0,0,0.12);
    overflow: hidden;
    font-family: "Open Sans", Arial, sans-serif;
  }
  .letterhead__header {
    position: absolute; left: 34px; right: 34px; top: 30px;
    display: flex; justify-content: space-between; align-items: flex-start;
  }
  .brand { display: flex; flex-direction: column; padding-top: 14px; }
  .brand__row { display: flex; align-items: center; gap: 7px; }
  .brand__square { width: 14px; height: 14px; background: var(--navy); flex: none; }
  .brand__name {
    font-weight: 700; font-size: 12px; line-height: 1;
    color: var(--navy); letter-spacing: 0.02em; white-space: nowrap;
  }
  .brand__tagline {
    margin-top: 7px; font-size: 6.5px; font-weight: 600;
    letter-spacing: 0.08em; color: var(--gray); white-space: nowrap;
  }
  .offices { display: flex; gap: 12px; }
  .office {
    font-style: normal;
    border-left: 1px solid var(--gray-light); padding-left: 8px;
    font-size: 6.5px; line-height: 1.45; color: var(--text); white-space: nowrap;
  }
  .office__title { font-weight: 700; color: var(--navy); font-size: 7px; }
  .office__line { display: flex; align-items: center; gap: 4px; }
  .office__icon { width: 7px; height: 7px; flex: none; }
  .letterhead__rule {
    position: absolute; left: 34px; right: 34px; top: 104px;
    height: 1px; background: var(--navy);
  }
  .letterhead__watermark {
    position: absolute; left: 50%; top: 250px;
    width: 150px; height: 150px; transform: translateX(-50%);
    background: var(--blue-pale); opacity: 0.7;
  }
  .letterhead__web {
    position: absolute; right: 60px; bottom: 44px;
    display: flex; align-items: center; gap: 6px;
    font-size: 8px; font-weight: 600; color: var(--navy); letter-spacing: 0.03em;
  }
  .letterhead__footer { position: absolute; left: 0; bottom: 0; width: 530px; height: 40px; }
</style>
</head>
<body>
<main class="canvas">
  <article class="letterhead">
    <header class="letterhead__header">
      <div class="brand">
        <div class="brand__row">
          <span class="brand__square"></span>
          <span class="brand__name">Ashford Kellan Moore</span>
        </div>
        <span class="brand__tagline">Counsel for Property Loss Claims</span>
      </div>
      <div class="offices">
        <address class="office">
          <div class="office__title">Riverside Office</div>
          <div>2280 Market Crossing, Suite 410</div>
          <div>Riverside, PA 19120</div>
          <div class="office__line">
            <svg class="office__icon" viewBox="0 0 10 10"><circle cx="5" cy="5" r="5" fill="#24508a"/><path d="M3.4 2.6l1 1-0.5 0.7a3.5 3.5 0 0 0 1.8 1.8l0.7-0.5 1 1-0.7 0.8C5 7.2 2.8 5 2.6 3.3z" fill="#fff"/></svg>
            (555) 210-4400
          </div>
          <div class="office__line">
            <svg class="office__icon" viewBox="0 0 10 10"><circle cx="5" cy="5" r="5" fill="#24508a"/><rect x="2.8" y="3" width="4.4" height="4" fill="#fff"/></svg>
            (555) 210-4401
          </div>
        </address>
        <address class="office">
          <div class="office__title">Lakeview Office</div>
          <div>760 Orchard Lane North, Suite 118</div>
          <div>Lakeview, NJ 08090</div>
          <div class="office__line">
            <svg class="office__icon" viewBox="0 0 10 10"><circle cx="5" cy="5" r="5" fill="#24508a"/><path d="M3.4 2.6l1 1-0.5 0.7a3.5 3.5 0 0 0 1.8 1.8l0.7-0.5 1 1-0.7 0.8C5 7.2 2.8 5 2.6 3.3z" fill="#fff"/></svg>
            (555) 388-7100
          </div>
          <div class="office__line">
            <svg class="office__icon" viewBox="0 0 10 10"><circle cx="5" cy="5" r="5" fill="#24508a"/><rect x="2.8" y="3" width="4.4" height="4" fill="#fff"/></svg>
            (555) 388-7101
          </div>
        </address>
      </div>
    </header>
    <div class="letterhead__rule"></div>
    <div class="letterhead__watermark" aria-hidden="true"></div>
    <div class="letterhead__web">
      <svg width="10" height="10" viewBox="0 0 10 10"><circle cx="5" cy="5" r="4.3" fill="none" stroke="#24508a" stroke-width="1"/><ellipse cx="5" cy="5" rx="1.8" ry="4.3" fill="none" stroke="#24508a" stroke-width="0.8"/><line x1="0.7" y1="5" x2="9.3" y2="5" stroke="#24508a" stroke-width="0.8"/></svg>
      www.akmlegal.com
    </div>
    <svg class="letterhead__footer" viewBox="0 0 530 40" preserveAspectRatio="none">
      <path d="M0 16 H250 Q260 16 264 24 Q268 30 278 30 H530 V40 H0 Z" fill="#24508a"/>
      <path d="M400 30 H530 V40 H400 Z" fill="#7a7d82"/>
    </svg>
  </article>
</main>
</body>
</html>
```